Flyer to Promote Membership in a Trade Association

UPDATE: I am looking for something modern and clean. NO CLIP ART. Not flashy. Just professional and modern. For everyone looking at our current flyer, we don't like it. That's why we aer looking for a new one. So please don't replicate it or use it as inspiration.

I need a flyer to promote membership in the Durable Residence Backers League. It can (probably should) be 2-sided. The content is attached as well as our logo and brand guidelines.

```html
<!DOCTYPE html>
<html lang="en">
<head>
<meta charset="utf-8">
<title>Durable Residence Backers League — Membership Flyer</title>
<link href="https://fonts.googleapis.com/css2?family=Merriweather:wght@700;900&family=Nunito+Sans:wght@300;400;700&display=swap" rel="stylesheet">
<style>
  :root{
    --backdrop:#2b2b2b;
    --paper:#f5f5f5;
    --orange:#ef7a2e;
    --slate:#5e6670;
    --muted:#8a9098;
    --rule:#d2d2d2;
  }
  *{margin:0;padding:0;box-sizing:border-box}
  html,body{width:1200px;height:768px;overflow:hidden;background:var(--backdrop)}
  .canvas{position:relative;width:1200px;height:768px;background:var(--backdrop)}
  .page{
    position:absolute;top:51px;width:513px;height:664px;overflow:hidden;
    background:
      linear-gradient(160deg,rgba(255,255,255,.9) 0%,rgba(255,255,255,0) 35%),
      linear-gradient(200deg,rgba(0,0,0,0) 55%,rgba(0,0,0,.05) 100%),
      var(--paper);
    font-family:"Nunito Sans",sans-serif;color:var(--slate);
  }
  .page--front{left:61px}
  .page--back{left:628px}
  .rules{position:absolute;inset:0;width:513px;height:664px}
  .rules line{stroke:var(--rule);stroke-width:1}
  .abs{position:absolute}
  .serif{font-family:"Merriweather",serif;font-weight:700;text-transform:uppercase}
  .orange{color:var(--orange)}

  .brand-mark{position:absolute;background:var(--orange)}
  .brand-word{position:absolute;font-family:"Nunito Sans",sans-serif;font-weight:700;color:var(--slate);letter-spacing:-1px;line-height:1;white-space:nowrap}
  .brand-name{position:absolute;font-family:"Merriweather",serif;font-weight:700;text-transform:uppercase;color:var(--muted);letter-spacing:.6px;border-left:1px solid var(--rule);white-space:nowrap}

  .front .brand-mark{left:45px;top:44px;width:38px;height:38px}
  .front .brand-word{left:92px;top:40px;font-size:46px}
  .front .brand-name{left:205px;top:38px;height:50px;padding-left:8px;font-size:8.6px;line-height:11.5px;padding-top:3px}
  .url{left:351px;top:57px;font-size:13px;color:var(--orange)}

  .headline{left:0;width:513px;top:127px;text-align:center;font-size:21.5px;line-height:23px}
  .headline .accent{color:var(--orange)}
  .intro{left:45px;top:257px;width:240px;font-size:12.4px;font-weight:300;line-height:16.2px}
  .stat{display:flex;align-items:center;gap:6px}
  .stat .num{font-family:"Merriweather",serif;font-weight:700;color:var(--orange);font-size:18px}
  .stat .label{font-size:11px;line-height:13px}
  .section-title{font-size:12.5px}
  .members-do{left:45px;top:386px}
  .members-do ul{list-style:none;margin-top:6px;font-size:12.3px;font-weight:300;line-height:16.1px}
  .promise{left:290px;width:192px;top:392px;text-align:center;font-size:14px;line-height:16.2px}
  .promise .team{margin-top:12px;color:var(--slate)}
  .join{left:0;width:513px;top:505px;text-align:center;font-size:13.5px}
  .tier p{font-size:12.3px;font-weight:300;line-height:16.2px}
  .tier .price{color:var(--orange);font-weight:400}

  .back .brand-mark{left:45px;top:49px;width:26px;height:26px}
  .back .brand-word{left:77px;top:46px;font-size:30px}
  .back .brand-name{left:150px;top:47px;height:30px;padding-left:4px;font-size:5.6px;line-height:7px;padding-top:1px}
  .ready{left:288px;top:52px;font-size:15px}
  .ready span{color:var(--slate)}
  .benefits-title{left:0;width:513px;top:102px;text-align:center;font-size:14px}
  .benefit-label{left:45px;font-size:10.6px;line-height:11.8px;color:var(--orange)}
  .benefit-text{width:270px;font-size:9.4px;font-weight:300;line-height:12.2px;color:var(--slate)}
  .roster-title{left:0;width:513px;top:508px;text-align:center;font-size:14px}
  .roster{left:10px;width:493px;top:527px;text-align:center;font-size:9.2px;font-weight:300;line-height:12.3px;white-space:nowrap}
  .roster b{color:var(--orange);font-weight:700}
</style>
</head>
<body>
<div class="canvas">

  <section class="page page--front front">
    <svg class="rules" viewBox="0 0 513 664" aria-hidden="true">
      <line x1="311" y1="31" x2="307" y2="113"/>
      <line x1="25" y1="113" x2="490" y2="113"/>
      <line x1="25" y1="237" x2="490" y2="237"/>
      <line x1="297" y1="237" x2="288" y2="372"/>
      <line x1="295" y1="284" x2="493" y2="284"/>
      <line x1="292" y1="324" x2="493" y2="324"/>
      <line x1="25" y1="372" x2="490" y2="372"/>
      <line x1="287" y1="372" x2="279" y2="498"/>
      <line x1="25" y1="498" x2="490" y2="498"/>
      <line x1="25" y1="527" x2="490" y2="527"/>
      <line x1="276" y1="527" x2="268" y2="631"/>
    </svg>

    <div class="brand-mark"></div>
    <div class="brand-word">DRBL</div>
    <div class="brand-name">Durable<br>Residence<br>Backers<br>League</div>
    <div class="abs url">www.drbl.org</div>

    <h1 class="abs headline serif">
      <span class="accent">Where LIHTC Investing<br>Excellence Begins</span><br>
      The Only Community Built<br>Exclusively for Investors
    </h1>

    <p class="abs intro">DRBL is where federal housing credit investors connect, learn, and lead. We are the only organization solely dedicated to LIHTC investors—giving you a trusted peer network, industry-setting standards, and the insights to stay informed.</p>

    <div class="abs stat" style="left:322px;top:250px"><span class="num">30</span><span class="label serif">Years of Impact</span></div>
    <div class="abs stat" style="left:318px;top:292px"><span class="num">60+</span><span class="label serif">Investor Firms</span></div>
    <div class="abs stat" style="left:314px;top:335px"><span class="num">1,000+</span><span class="label serif">Industry<br>Professionals</span></div>

    <div class="abs members-do">
      <h2 class="section-title serif orange">What Members Do</h2>
      <ul>
        <li><span class="orange">Network</span>: Peer Groups &amp; Forums</li>
        <li><span class="orange">Learn</span>: Conferences &amp; Webinars</li>
        <li><span class="orange">Share</span>: Candid Investor Exchange</li>
        <li><span class="orange">Shape</span>: Standards &amp; Best Practices</li>
        <li><span class="orange">Grow</span>: Professional Development</li>
      </ul>
    </div>

    <div class="abs promise serif">
      <p class="orange">One Membership,<br>Unlimited Access.</p>
      <p class="team">Your Entire Team<br>Can Participate in<br>DRBL Activities.</p>
    </div>

    <h2 class="abs join serif orange">Join DRBL Today</h2>

    <div class="abs tier" style="left:45px;top:542px">
      <h3 class="section-title serif orange" style="margin-bottom:5px">Investor Members</h3>
      <p>Banks, Insurance Companies,<br>Economic Investors</p>
      <p class="price">$5,000/year (assets ≥$5B)<br>$1,000/year (assets &lt;$5B)</p>
    </div>
    <div class="abs tier" style="left:303px;top:543px">
      <h3 class="section-title serif orange" style="margin-bottom:5px">Affiliate Members</h3>
      <p>Syndicators &amp; Brokers</p>
      <p class="price">$4,500/year</p>
    </div>
  </section>

  <section class="page page--back back">
    <svg class="rules" viewBox="0 0 513 664" aria-hidden="true">
      <line x1="216" y1="31" x2="211" y2="96"/>
      <line x1="20" y1="97" x2="493" y2="97"/>
      <line x1="20" y1="125" x2="493" y2="125"/>
      <line x1="20" y1="183.5" x2="493" y2="183.5"/>
      <line x1="20" y1="232" x2="493" y2="232"/>
      <line x1="20" y1="280" x2="493" y2="280"/>
      <line x1="20" y1="340" x2="493" y2="340"/>
      <line x1="20" y1="388.5" x2="493" y2="388.5"/>
      <line x1="20" y1="445" x2="493" y2="445"/>
      <line x1="20" y1="501" x2="493" y2="501"/>
      <line x1="209" y1="125" x2="181" y2="501"/>
      <line x1="20" y1="616" x2="493" y2="616"/>
      <line x1="172" y1="617" x2="171" y2="632"/>
    </svg>

    <div class="brand-mark"></div>
    <div class="brand-word">DRBL</div>
    <div class="brand-name">Durable<br>Residence<br>Backers<br>League</div>
    <div class="abs ready orange">Ready to join? <span>drbl.org</span></div>

    <h2 class="abs benefits-title serif">Member Benefits</h2>

    <h3 class="abs benefit-label serif" style="top:143px">Members-Only<br>Conferences</h3>
    <p class="abs benefit-text" style="left:222px;top:135px">Two annual in-person meetings. Spring Meeting: investors-only for candid peer conversations. Fall Summit: full ecosystem gathering with syndicators and brokers.</p>

    <h3 class="abs benefit-label serif" style="top:203px">Investor-Only Forums</h3>
    <p class="abs benefit-text" style="left:217px;top:197px">Exclusive meetings and webinars for investors only, enabling candid conversations and meaningful collaboration.</p>

    <h3 class="abs benefit-label serif" style="top:251px">Peer-to-Peer Meetups</h3>
    <p class="abs benefit-text" style="left:213px;top:245px">Find your peers—underwriters, asset managers, credit officers and more—with our meetups.</p>

    <h3 class="abs benefit-label serif" style="top:298px">Live &amp; On-Demand<br>Webinars</h3>
    <p class="abs benefit-text" style="left:210px;top:292px">Free monthly Third Thursday webinars covering Year 15 issues, secondary transactions, securitizing developer fees and other emerging topics.</p>

    <h3 class="abs benefit-label serif" style="top:353px">Searchable Member<br>Directory</h3>
    <p class="abs benefit-text" style="left:204px;top:353px;width:280px">Find underwriters, asset managers, and credit officers—searchable by role, firm type, and investment approach.</p>

    <h3 class="abs benefit-label serif" style="top:400px">Shape Industry<br>Standards<br>[Investor Only]</h3>
    <p class="abs benefit-text" style="left:199px;top:405px;width:285px">DRBL’s underwriting and asset management standards are adopted industry-wide. Influence them through our committees.</p>

    <h3 class="abs benefit-label serif" style="top:456px">Emerging Leaders<br>Program<br>[Investor Only]</h3>
    <p class="abs benefit-text" style="left:195px;top:461px;width:285px">Develop your firm’s next-generation leaders through dedicated professional development programming.</p>

    <h2 class="abs roster-title serif">Our Investor Members Include</h2>
    <p class="abs roster">
      <b>•</b> Harborline Life/Crestwell Health <b>•</b> Keystone Bank <b>•</b> Meridian Federal National Bank <b>•</b> Bank of Northfield<br>
      <b>•</b> Granite Ridge Bank <b>•</b> Prairie Financial <b>•</b> Summit One <b>•</b> Lakeshore Trust Bank <b>•</b> CRTB <b>•</b> Fourth Street CDC<br>
      <b>•</b> Pioneer Citizens Bank <b>•</b> Ashford Partners <b>•</b> Cornerstone Bank <b>•</b> Whitfield Capital<br>
      <b>•</b> Statewide Mutual Insurance <b>•</b> Hudson Life <b>•</b> Alder (Teachers Fund) <b>•</b> Ridgeway Real Estate<br>
      <b>•</b> Regional Housing Partners <b>•</b> Seabright Bank <b>•</b> Brightcoat Paints <b>•</b> Tidewater Bank <b>•</b> Towncrest Bank<br>
      <b>•</b> Trueline Community Capital <b>•</b> Alpine Bank USA <b>•</b> Veterans Mutual <b>•</b> Union Bancorp Impact Finance<br>
      <b>•</b> Oakridge Bank
    </p>
  </section>

</div>
</body>
</html>
```